Business Card Design Project

We consult with hotels on setting rates and maximizing a revenue strategy

Industry/Entity Type

Business

Contact Information for Business Card

I am not sure what I want. Our company offers high level consulting to hotels around the country but we are also laid back. I would like something that is professional but also shows the laid back side

```html
<!DOCTYPE html>
<html lang="en">
<head>
<meta charset="utf-8">
<title>Keystone Revenue Management Solutions – Business Cards</title>
<link href="https://fonts.googleapis.com/css2?family=PT+Sans+Narrow:wght@400;700&display=swap" rel="stylesheet">
<style>
  :root {
    --backdrop: #1c1c1d;
    --card-white: #ffffff;
    --mist: #eef3f3;
    --aqua-light: #bfe7e8;
    --aqua: #93d4d6;
    --teal: #2a7c79;
    --teal-deep: #1f6664;
    --brown: #3b2a22;
    --ink: #1d1d1d;
    --rule: #8fa9a9;
  }
  * { box-sizing: border-box; margin: 0; padding: 0; }
  html, body {
    width: 1200px; height: 800px; overflow: hidden;
    background: var(--backdrop);
    font-family: "PT Sans Narrow", "Arial Narrow", sans-serif;
  }
  .canvas {
    position: relative; width: 1200px; height: 800px;
    display: flex; align-items: center; justify-content: center; gap: 50px;
  }
  .card {
    position: relative; width: 525px; height: 300px; overflow: hidden;
    border-radius: 3px;
    box-shadow: 0 14px 30px rgba(0,0,0,.55);
  }
  /* Front */
  .card--front {
    background: linear-gradient(165deg, var(--card-white) 0%, var(--card-white) 40%, var(--mist) 60%, #9cc6c4 85%, var(--teal) 100%);
  }
  .front-lockup {
    position: absolute; left: 120px; top: 112px;
  }
  .front-lockup .web {
    font-weight: 700; font-size: 15px; color: var(--ink);
    text-align: right; margin-bottom: 2px;
  }
  .brand {
    display: flex; align-items: center; gap: 10px;
    font-weight: 700; color: var(--brown); letter-spacing: 2px; line-height: 1;
  }
  .brand-mark { width: 22px; height: 22px; background: var(--teal); }
  .front-lockup .brand { font-size: 52px; }
  .front-lockup .tagline {
    display: inline-block; margin-top: 4px; margin-left: 32px;
    background: var(--brown); color: var(--card-white);
    font-weight: 700; font-size: 17px; padding: 2px 14px;
  }
  /* Back */
  .card--back {
    background: linear-gradient(160deg, var(--card-white) 0%, var(--card-white) 42%, var(--aqua-light) 62%, var(--aqua) 100%);
  }
  .back-info {
    position: absolute; right: 28px; top: 34px; width: 300px; text-align: right;
    color: var(--ink);
  }
  .back-info .brand { justify-content: flex-end; font-size: 40px; }
  .back-info .brand-mark { width: 18px; height: 18px; }
  .back-info .tagline {
    color: var(--teal-deep); font-weight: 700; font-size: 19px; margin-top: 2px;
  }
  .rule { border-top: 1px dashed var(--rule); margin: 10px 0; }
  .person-name { font-weight: 700; font-size: 18px; color: var(--brown); }
  .person-title { font-size: 13px; color: var(--teal-deep); }
  .contact { list-style: none; font-size: 16px; line-height: 1.3; }
</style>
</head>
<body>
<main class="canvas">
  <section class="card card--front" aria-label="Card front">
    <div class="front-lockup">
      <p class="web">www.KeystoneRMS.com</p>
      <div class="brand"><span class="brand-mark"></span>KEYSTONE</div>
      <p class="tagline">Revenue Management Solutions</p>
    </div>
  </section>

  <section class="card card--back" aria-label="Card back">
    <div class="back-info">
      <div class="brand"><span class="brand-mark"></span>KEYSTONE</div>
      <p class="tagline">Revenue Management Solutions</p>
      <div class="rule"></div>
      <p class="person-name">DANA WHITFIELD</p>
      <p class="person-title">Regional Revenue Manager</p>
      <div class="rule"></div>
      <ul class="contact">
        <li>Office: 555-014-2200</li>
        <li>Fax: 555-014-3800</li>
        <li>Email: dana@KeystoneRMS.com</li>
        <li>www.KeystoneRMS.com</li>
      </ul>
      <div class="rule"></div>
    </div>
  </section>
</main>
</body>
</html>
```